Design required for boutique fire engineering firm in New Zealand

Our website was published based on free Wordpress templates, we'd like something a bit more bespoke, clean and simple.

Reason: didn't check this finished on a Sunday :)

Target Market(s)

architects, building owners, property developers

Industry/Entity Type

Boutique

Contact Information for Business Card

Logo
Fire Engineering

Derek Holloway
Principal
+64 21 738 152
derek@veltraxa.nz
veltraxa.nz

Number of Pages Required

3 page

Font styles to use
Sans Serif

Requirements
Nice to have
• On the business card, an embossed logo would be great - not sure if that's a design thing or just a print thing?
• Website, existing @ http://veltraxa.nz for extent of content and general arrangement that I'm happy with.
• Ability to update the content with project bio's and some photos at a later date would be nice.

```html
<!DOCTYPE html>
<html lang="en">
<head>
<meta charset="utf-8">
<title>Veltraxa — Fire Engineering</title>
<link href="https://fonts.googleapis.com/css2?family=Raleway:wght@400;500;600;700&display=swap" rel="stylesheet">
<style>
:root{
  --blue:#2f73b5;
  --blue-deep:#1c5ea0;
  --navy:#0d4a7e;
  --ink:#222428;
  --text:#3c3f44;
  --white:#ffffff;
  --footer:#3a3b3d;
  --tile-red:#b8252c;
  --tile-grey:#c9ccd2;
}
*{margin:0;padding:0;box-sizing:border-box}
html,body{width:1200px;height:3147px;overflow:hidden;background:var(--white)}
body{position:relative;font-family:'Raleway',Arial,sans-serif;color:var(--text)}
.abs{position:absolute}

/* header */
.site-header{left:0;top:0;width:1200px;height:80px;background:var(--white)}
.brand{left:99px;top:20px;display:flex;align-items:center;gap:10px}
.brand-mark{width:36px;height:36px;border-radius:50%;background:var(--blue-deep)}
.brand-name{font-size:31px;font-weight:700;color:var(--blue-deep);letter-spacing:0.2px}
.nav{left:0;top:0;width:1200px;height:80px}
.nav a{position:absolute;top:31px;font-size:13px;font-weight:500;color:var(--ink);text-decoration:none;letter-spacing:.3px}
.nav a.active{color:var(--blue)}
.nav-underline{left:598px;top:76px;width:50px;height:3px;background:var(--blue)}
.search{left:1074px;top:26px}

/* hero */
.hero{left:0;top:80px;width:1200px;height:447px;background:linear-gradient(135deg,#5a6a7c 0%,#8e2a30 35%,#c1313a 55%,#6b7380 80%,#3f4650 100%)}
.hero-shade{left:0;top:80px;width:1200px;height:447px;background:rgba(20,30,45,.35)}
.hero-title{left:0;top:198px;width:1200px;text-align:center;font-size:27px;font-weight:600;color:var(--white);line-height:38px;text-transform:uppercase}
.hero-sub{left:0;top:298px;width:1200px;text-align:center;font-size:13px;color:var(--white)}
.btn-hero{top:373px;height:45px;width:178px;background:var(--blue);color:var(--white);font-size:14px;display:flex;align-items:center;justify-content:center}

/* about */
.section-title{font-size:23px;font-weight:700;color:var(--ink);text-transform:uppercase}
.section-title span{color:var(--blue)}
.about-title{left:141px;top:566px}
.about-title span{color:var(--blue-deep)}
.about-title b{font-weight:600;color:var(--ink)}
.about-lead{left:139px;top:616px;width:440px;font-size:20px;line-height:24px;color:var(--ink)}
.about-lead strong{color:var(--blue-deep);font-weight:600}
.about-body{left:139px;top:706px;width:410px;font-size:13px;line-height:17.5px;color:var(--text)}
.btn-small{left:141px;top:814px;width:100px;height:29px;background:var(--blue);color:var(--white);font-size:11px;display:flex;align-items:center;justify-content:center;border-radius:2px}
.about-photo{left:617px;top:571px;width:443px;height:270px;background:linear-gradient(135deg,#9aa3ad 0%,#e8c43a 30%,#3a4452 60%,#c7352c 85%)}

/* services */
.center-title{left:0;width:1200px;text-align:center}
.services-title{top:928px}
.service-card{width:321px;height:258px;background:linear-gradient(160deg,var(--tile-grey) 0%,#e5e6ea 30%,var(--tile-red) 55%,#d4454a 75%,#aeb3bb 100%)}
.service-label{position:absolute;left:0;bottom:0;width:100%;height:57px;background:rgba(47,115,181,.88);color:var(--white);font-size:17px;font-weight:600;display:flex;align-items:center;justify-content:center}

/* why choose us */
.why-photo{left:0;top:1615px;width:510px;height:475px;background:linear-gradient(120deg,#7fa25a 0%,#b9c48f 25%,#2d2f33 55%,#c52a2e 80%,#8e9a6a 100%)}
.why-panel{left:510px;top:1615px;width:690px;height:475px;background:var(--blue)}
.why-title{left:558px;top:1656px;font-size:23px;font-weight:700;color:var(--white)}
.why-body{left:560px;top:1700px;width:490px;font-size:13.5px;line-height:22px;color:var(--white)}
.why-list{left:560px;top:1818px;list-style:none}
.why-list li{display:flex;align-items:center;gap:14px;height:45px;font-size:13.5px;color:var(--white)}
.btn-outline{left:560px;top:2010px;width:128px;height:36px;background:var(--white);color:var(--blue);font-size:12px;display:flex;align-items:center;justify-content:center}

/* projects */
.projects-title{top:2130px}
.project-tile{top:2197px;width:321px;height:256px;background:linear-gradient(150deg,#d7dade 0%,#c72a31 35%,#e0474d 55%,#9a9fa7 80%,#e6e7ea 100%)}
.project-overlay{left:101px;top:2197px;width:321px;height:256px;background:rgba(47,115,181,.85)}
.project-plus{left:225px;top:2280px}

/* contact */
.contact{left:0;top:2566px;width:1200px;height:535px;background:var(--navy)}
.contact-title{top:2604px;font-size:23px;font-weight:700;color:var(--white)}
.field{left:237px;width:355px;border:1px solid rgba(255,255,255,.75);color:var(--white);font-size:13px;padding:10px 20px}
.btn-submit{left:237px;top:3006px;width:139px;height:45px;background:var(--white);color:var(--navy);font-size:14px;font-weight:600;display:flex;align-items:center;justify-content:center}
.contact-note{left:644px;top:2688px;width:350px;font-size:13.5px;line-height:19px;color:var(--white)}
.contact-card{left:644px;top:2805px;font-size:17px;line-height:24px;color:var(--white);letter-spacing:.4px}
.social{top:2897px;width:33px;height:33px;border-radius:50%;background:#4aa3e6}
.social.square{border-radius:4px;background:#2d8dcc;width:31px;height:31px;top:2898px}

/* footer */
.site-footer{left:0;top:3101px;width:1200px;height:46px;background:var(--footer)}
.copyright{left:760px;top:3114px;font-size:14px;color:var(--white);font-weight:500}
</style>
</head>
<body>

<header class="abs site-header">
  <div class="abs brand"><span class="brand-mark"></span><span class="brand-name">veltraxa</span></div>
  <nav class="abs nav">
    <a class="active" style="left:604px">HOME</a>
    <a style="left:676px">ABOUT US</a>
    <a style="left:778px">SERVICES</a>
    <a style="left:873px">CLIENTS</a>
    <a style="left:959px">CONTACT US</a>
  </nav>
  <div class="abs nav-underline"></div>
  <svg class="abs search" width="24" height="24" viewBox="0 0 24 24" fill="none" stroke="#444" stroke-width="2"><circle cx="10" cy="10" r="7"/><line x1="15" y1="15" x2="21" y2="21"/></svg>
</header>

<section>
  <div class="abs hero" role="img" aria-label="Photograph of a red fire pump room with valves and pipework"></div>
  <div class="abs hero-shade"></div>
  <h1 class="abs hero-title">Offering a reliable and efficient fire fighting systems<br>to residential and commercial industries</h1>
  <p class="abs hero-sub">Lorem Ipsum is simply dummy text of the printing and typesetting industry.</p>
  <a class="abs btn-hero" style="left:365px">Learn More</a>
  <a class="abs btn-hero" style="left:619px">Our Services</a>
</section>

<section>
  <h2 class="abs section-title about-title"><span>About</span> <b>Us</b></h2>
  <p class="abs about-lead">Welcome we are <strong>Veltraxa</strong> lorem Ipsum is simply dummy text of the printing and typesetting industry.</p>
  <p class="abs about-body">Lorem Ipsum is simply dummy text of the printing and typesetting industry. Lorem Ipsum has been the industry's standard dummy text ever since the 1500s, when an unknown printer took a galley of type and scrambled it to make a type specimen book.</p>
  <a class="abs btn-small">Know More</a>
  <div class="abs about-photo" role="img" aria-label="Photograph of firefighters in helmets checking a control panel"></div>
</section>

<section>
  <h2 class="abs section-title center-title services-title">Our <span>Services</span></h2>
  <div class="abs service-card" style="left:99px;top:994px" role="img" aria-label="Photograph of fire pump equipment"><div class="service-label">Fire Fighting Systems</div></div>
  <div class="abs service-card" style="left:438px;top:994px" role="img" aria-label="Photograph of fire pump equipment"><div class="service-label">Hydrant System</div></div>
  <div class="abs service-card" style="left:776px;top:994px" role="img" aria-label="Photograph of fire pump equipment"><div class="service-label">Sprinklers</div></div>
  <div class="abs service-card" style="left:99px;top:1294px" role="img" aria-label="Photograph of fire pump equipment"><div class="service-label">Alarm System</div></div>
  <div class="abs service-card" style="left:438px;top:1294px" role="img" aria-label="Photograph of fire pump equipment"><div class="service-label">Pumping Systems</div></div>
  <div class="abs service-card" style="left:776px;top:1294px" role="img" aria-label="Photograph of fire pump equipment"><div class="service-label">Fire Extinguishers</div></div>
</section>

<section>
  <div class="abs why-photo" role="img" aria-label="Photograph of a firefighter holding a red helmet beside a fire truck"></div>
  <div class="abs why-panel"></div>
  <h2 class="abs why-title">WHY CHOOSE US</h2>
  <p class="abs why-body">Lorem Ipsum is simply dummy text of the printing and typesetting ndustry. Lorem Ipsum has been the industry's standard dummy text since the 1500s, when an unknown printer took a galley of type and crambled it to make a type specimen book.</p>
  <ul class="abs why-list">
    <li><svg width="26" height="26" viewBox="0 0 26 26" fill="none" stroke="#fff" stroke-width="1.6"><circle cx="13" cy="13" r="11.5"/><polyline points="8,13.5 11.5,17 18,9.5"/></svg>Superior Quality Products</li>
    <li><svg width="26" height="26" viewBox="0 0 26 26" fill="none" stroke="#fff" stroke-width="1.6"><circle cx="13" cy="13" r="11.5"/><polyline points="8,13.5 11.5,17 18,9.5"/></svg>Lifetime Support</li>
    <li><svg width="26" height="26" viewBox="0 0 26 26" fill="none" stroke="#fff" stroke-width="1.6"><circle cx="13" cy="13" r="11.5"/><polyline points="8,13.5 11.5,17 18,9.5"/></svg>Customer Satisfaction Guarenteed</li>
    <li><svg width="26" height="26" viewBox="0 0 26 26" fill="none" stroke="#fff" stroke-width="1.6"><circle cx="13" cy="13" r="11.5"/><polyline points="8,13.5 11.5,17 18,9.5"/></svg>Superior Quality Products</li>
  </ul>
  <a class="abs btn-outline">LEARN MORE</a>
</section>

<section>
  <h2 class="abs section-title center-title projects-title">Our <span>Projects</span></h2>
  <div class="abs project-tile" style="left:101px" role="img" aria-label="Photograph of a plant room"></div>
  <div class="abs project-overlay"></div>
  <svg class="abs project-plus" width="72" height="72" viewBox="0 0 72 72" fill="none" stroke="#fff" stroke-width="2"><circle cx="36" cy="36" r="34"/><line x1="36" y1="18" x2="36" y2="54"/><line x1="18" y1="36" x2="54" y2="36"/></svg>
  <div class="abs project-tile" style="left:441px" role="img" aria-label="Photograph of red fire pump sets"></div>
  <div class="abs project-tile" style="left:778px" role="img" aria-label="Photograph of red fire pump sets"></div>
</section>

<section>
  <div class="abs contact"></div>
  <h2 class="abs center-title contact-title">CONTACT US</h2>
  <div class="abs field" style="top:2698px;height:44px">Your Name</div>
  <div class="abs field" style="top:2765px;height:46px">Your Email</div>
  <div class="abs field" style="top:2834px;height:141px">Your Message</div>
  <a class="abs btn-submit">SUBMIT</a>
  <p class="abs contact-note">Lorem ipsum dolor sit amet, consectetuer adipiscing elit. Donec odio. Quisque volutpat mattis eros. Nullam malesuada erat ut turpis. Suspendisse urna nibh, viverra non, semper suscipit, posuere a, pede.</p>
  <p class="abs contact-card">Derek Holloway<br>Principal, Fire Engineer<br>021 738 152</p>
  <span class="abs social" style="left:640px"></span>
  <span class="abs social square" style="left:689px"></span>
</section>

<footer class="abs site-footer"></footer>
<p class="abs copyright">© 2017 Veltraxa . All Rights Reserved.</p>

</body>
</html>
```